Contractor Business Card Design

Looking to have a card made that has a bold description of (KITCHENS, BASEMENTS, BATHROOMS)

Definition and layers a plus

Contact info is;

Mark T. Ellery
Maple Bend, MN 55012
Cell: 612-555-0147
website: www.cobaltfinishworks.example
Email: cobaltfinishworksmn@mailbox.example

colors: red, black, gray, white

Contact Information for Business Card

Contact info is;

Mark T. Ellery
Maple Bend, MN 55012
Cell: 612-555-0147

Colors
ec1f27

Requirements
Must have
• Looking for layers and definition
Nice to have
• Cards are planned to be printed on plastic cards

```html
<!DOCTYPE html>
<html lang="en">
<head>
<meta charset="utf-8">
<title>Cobalt Finish Works – Business Card</title>
<link href="https://fonts.googleapis.com/css2?family=Montserrat:wght@400;500;700&display=swap" rel="stylesheet">
<style>
  :root {
    --page-bg: #e4e0db;
    --card-top: #f4f3f2;
    --card-bottom: #d9d7d5;
    --band-black: #111112;
    --band-black-soft: #2a2a2c;
    --brand-red: #ec1f27;
    --deep-red: #c1272d;
    --ink: #2b2b2b;
    --ink-soft: #4a4a4a;
    --white: #ffffff;
  }
  * { margin: 0; padding: 0; box-sizing: border-box; }
  html, body {
    width: 1200px; height: 970px; overflow: hidden;
    background: var(--page-bg);
    font-family: "Montserrat", sans-serif;
  }
  .card {
    position: absolute; left: 60px; top: 185px;
    width: 1080px; height: 600px;
    border-radius: 26px; overflow: hidden;
    background: linear-gradient(160deg, var(--card-top) 0%, #e9e8e6 50%, var(--card-bottom) 100%);
    box-shadow: 0 18px 40px rgba(0,0,0,0.18), 0 0 0 1px rgba(0,0,0,0.08);
  }
  .top-band {
    position: absolute; left: 0; top: 0; width: 100%; height: 172px;
    background: linear-gradient(180deg, var(--band-black) 0%, var(--band-black-soft) 100%);
  }
  .rule {
    position: absolute; left: 0; top: 172px; width: 100%; height: 8px;
    background: linear-gradient(180deg, var(--white) 0 3px, var(--deep-red) 3px 8px);
  }
  .services {
    position: absolute; left: 57px; top: 80px;
    font-size: 29px; font-weight: 500; color: var(--brand-red);
    letter-spacing: 0.5px; white-space: nowrap;
  }
  .services .divider { color: #8a8a8a; margin: 0 12px; font-weight: 400; }
  .brand-mark {
    position: absolute; left: 750px; top: 42px;
    width: 220px; height: 220px;
  }
  .brand-name {
    position: absolute; left: 640px; top: 292px; width: 440px;
    text-align: center; white-space: nowrap;
    font-size: 32px; font-weight: 700; color: var(--band-black);
    letter-spacing: 0.5px; text-transform: uppercase; line-height: 1.2;
  }
  .holder-name {
    position: absolute; left: 57px; top: 325px;
    font-size: 39px; font-weight: 700; color: var(--ink);
  }
  .contact-list {
    position: absolute; left: 57px; top: 405px; list-style: none;
  }
  .contact-list li {
    display: flex; align-items: center; height: 36px;
    font-size: 23px; font-weight: 400; color: var(--ink-soft);
  }
  .contact-list svg { width: 24px; height: 24px; margin-right: 12px; fill: var(--deep-red); flex: none; }
</style>
</head>
<body>
  <div class="card">
    <div class="top-band"></div>
    <div class="rule"></div>

    <p class="services">Kitchens<span class="divider">|</span>Basements<span class="divider">|</span>Bathrooms</p>

    <svg class="brand-mark" viewBox="0 0 220 220" aria-hidden="true">
      <circle cx="110" cy="110" r="100" fill="#f2f1f0" stroke="var(--deep-red)" stroke-width="6"/>
    </svg>

    <p class="brand-name">Cobalt Finish Works</p>

    <h1 class="holder-name">Mark T. Ellery</h1>

    <ul class="contact-list">
      <li>
        <svg viewBox="0 0 24 24"><path d="M12 2a7 7 0 0 0-7 7c0 5.2 7 13 7 13s7-7.8 7-13a7 7 0 0 0-7-7zm0 9.6A2.6 2.6 0 1 1 12 6.4a2.6 2.6 0 0 1 0 5.2z"/></svg>
        Maple Bend, MN 55012
      </li>
      <li>
        <svg viewBox="0 0 24 24"><path d="M6.6 10.8a15.2 15.2 0 0 0 6.6 6.6l2.2-2.2a1 1 0 0 1 1-.25 11.4 11.4 0 0 0 3.6.57 1 1 0 0 1 1 1V20a1 1 0 0 1-1 1A17 17 0 0 1 3 4a1 1 0 0 1 1-1h3.5a1 1 0 0 1 1 1c0 1.25.2 2.45.57 3.57a1 1 0 0 1-.25 1z"/></svg>
        612-555-0147
      </li>
      <li>
        <svg viewBox="0 0 24 24"><path d="M2 5h20v2.2l-10 6-10-6zM2 9.6l10 6 10-6V19H2z"/></svg>
        cobaltfinishworksmn@mailbox.example
      </li>
      <li>
        <svg viewBox="0 0 24 24"><path d="M12 2a10 10 0 1 0 0 20 10 10 0 0 0 0-20zm6.9 6h-2.9a15.6 15.6 0 0 0-1.4-3.6A8 8 0 0 1 18.9 8zM12 4c.8 1.2 1.5 2.5 1.9 4h-3.8c.4-1.5 1.100-2.8 1.900-4zM4.3 14a8 8 0 0 1 0-4h3.4a16.5 16.5 0 0 0 0 4zm.8 2h2.9a15.6 15.6 0 0 0 1.4 3.6A8 8 0 0 1 5.1 16zM8 8H5.1a8 8 0 0 1 4.3-3.6A15.6 15.6 0 0 0 8 8zm4 12c-.8-1.2-1.5-2.5-1.9-4h3.8c-.4 1.5-1.1 2.8-1.9 4zm2.3-6H9.7a14.7 14.7 0 0 1 0-4h4.6a14.7 14.7 0 0 1 0 4zm.3 5.6a15.6 15.6 0 0 0 1.4-3.6h2.9a8 8 0 0 1-4.3 3.6zm1.7-5.6a16.5 16.5 0 0 0 0-4h3.4a8 8 0 0 1 0 4z"/></svg>
        www.cobaltfinishworks.example
      </li>
    </ul>
  </div>
</body>
</html>
```